Pagewall, Blipster and Crewnest cover image design

Looking to update the pagewall, blipster and aLinkedin cover images for Halvard Ledger . website www.halvledger-example.com
https://www.crewnest-example.com/company/halvard-ledger-llc/mycompany/?viewAsMember=true
https://www.pagewall-example.com/halvledger
https://blipster-example.com/halvledger

```html
<!DOCTYPE html>
<html lang="en">
<head>
<meta charset="utf-8">
<title>Halvard Ledger – Social Cover Set</title>
<link href="https://fonts.googleapis.com/css2?family=Oswald:wght@500&family=Montserrat:wght@400;600;700&family=Roboto:wght@400&display=swap" rel="stylesheet">
<style>
  :root {
    --board: #e3e3e3;
    --green: #4a9a3f;
    --green-deep: #3b8433;
    --ink: #76776b;
    --body-ink: #7c7d73;
    --label-ink: #3c3c3c;
    --white: #ffffff;
    --photo-light: #f4f4f4;
    --photo-mid: #dcdcdc;
  }
  * { margin: 0; padding: 0; box-sizing: border-box; }
  html, body { width: 1200px; height: 1180px; overflow: hidden; }
  body { background: var(--board); position: relative; font-family: "Montserrat", sans-serif; }

  .cover-label { position: absolute; left: 99px; font-family: "Roboto", sans-serif; font-size: 15px; color: var(--label-ink); }

  .cover { position: absolute; left: 99px; background: var(--white); overflow: hidden; box-shadow: 0 3px 6px rgba(0,0,0,.28); }
  .cover-blipster { top: 69px; width: 950px; height: 316px; }
  .cover-crewnest { top: 511px; width: 1003px; height: 250px; }
  .cover-pagewall { top: 903px; width: 539px; height: 200px; }

  .backdrop { position: absolute; inset: 0; }
  .office-photo { position: absolute; inset: 0; background: linear-gradient(100deg, var(--photo-mid) 0%, var(--photo-light) 35%, #e6e6e6 60%, #f0f0f0 100%); opacity: .8; }
  .shapes { position: absolute; inset: 0; width: 100%; height: 100%; }

  .brand { position: absolute; display: flex; align-items: center; gap: .25em; }
  .brand-square { width: 1.55em; height: 1.55em; background: var(--green); flex: none; }
  .brand-name { font-family: "Montserrat", sans-serif; font-weight: 700; color: var(--ink); line-height: .95; font-size: .62em; text-transform: uppercase; letter-spacing: -.01em; }

  .headline { position: absolute; font-family: "Oswald", sans-serif; font-weight: 500; color: var(--ink); line-height: 1; white-space: nowrap; letter-spacing: -.01em; }
  .headline .accent { color: var(--green); }

  .pitch { position: absolute; color: var(--body-ink); white-space: nowrap; }
  .pitch strong { color: var(--green); font-weight: 700; }

  .call-box { position: absolute; background: var(--green); color: var(--white); display: flex; align-items: center; justify-content: center; white-space: nowrap; }
  .call-box b { font-weight: 700; margin-left: .3em; }

  .partner { position: absolute; color: var(--white); text-align: center; white-space: nowrap; }
  .partner-name { display: block; font-weight: 700; border-bottom: 1.5px solid var(--white); line-height: 1.15; }
  .partner-tag { display: block; line-height: 1.3; }
  .partner-bold .partner-tag { font-weight: 700; }

  .inset-photo { position: absolute; border: 4px solid var(--white); background: linear-gradient(170deg, #e9e9e9 0%, #c9c9c9 30%, #4c4f57 55%, #3a3c42 70%, #eeeeee 85%, #f6f6f6 100%); box-shadow: 0 2px 6px rgba(0,0,0,.3); }
  .inset-bracket { position: absolute; border-left: 2px solid var(--green); border-bottom: 2px solid var(--green); }

  .social { position: absolute; display: flex; }
  .social span { border-radius: 50%; background: var(--white); }

  .avatar { position: absolute; border-radius: 50%; background: var(--white); border: 2px solid var(--green); box-shadow: 0 0 0 4px var(--white), 0 3px 7px 4px rgba(0,0,0,.22); }
  .avatar .brand { left: 50%; top: 50%; transform: translate(-50%, -50%); }

  /* Blipster */
  .cover-blipster .brand { left: 17px; top: 14px; font-size: 26px; }
  .cover-blipster .headline { font-size: 46px; }
  .cover-blipster .line-one { left: 64px; top: 80px; }
  .cover-blipster .line-two { left: 144px; top: 133px; }
  .cover-blipster .pitch { left: 252px; top: 192px; font-size: 12.4px; line-height: 15.5px; }
  .cover-blipster .call-box { left: 345px; top: 249px; width: 226px; height: 23px; font-size: 13px; }
  .cover-blipster .call-box b { font-size: 16px; }
  .cover-blipster .partner { top: 15px; font-size: 18px; }
  .cover-blipster .partner-tag { font-size: 8.4px; }
  .cover-blipster .partner-one { left: 712px; width: 100px; }
  .cover-blipster .partner-two { left: 825px; width: 99px; }
  .cover-blipster .inset-photo { left: 668px; top: 126px; width: 157px; height: 156px; }
  .cover-blipster .inset-bracket { left: 659px; top: 236px; width: 51px; height: 51px; }
  .cover-blipster .social { left: 850px; top: 280px; gap: 8px; }
  .cover-blipster .social span { width: 21px; height: 21px; }
  .avatar-blipster { left: 166px; top: 299px; width: 146px; height: 146px; }
  .avatar-blipster .brand { font-size: 25px; }

  /* Crewnest */
  .cover-crewnest .brand { left: 13px; top: 16px; font-size: 28px; }
  .cover-crewnest .headline { font-size: 46px; }
  .cover-crewnest .line-one { left: 179px; top: 25px; }
  .cover-crewnest .line-two { left: 259px; top: 78px; }
  .cover-crewnest .pitch { left: 367px; top: 135px; font-size: 12.4px; line-height: 15.5px; }
  .cover-crewnest .call-box { left: 459px; top: 193px; width: 226px; height: 22px; font-size: 13px; }
  .cover-crewnest .call-box b { font-size: 16px; }
  .cover-crewnest .partner { top: 12px; font-size: 14px; }
  .cover-crewnest .partner-tag { font-size: 6.8px; }
  .cover-crewnest .partner-one { left: 816px; width: 80px; }
  .cover-crewnest .partner-two { left: 905px; width: 80px; }
  .cover-crewnest .inset-photo { left: 781px; top: 99px; width: 124px; height: 123px; }
  .cover-crewnest .inset-bracket { left: 774px; top: 186px; width: 41px; height: 41px; }
  .cover-crewnest .social { left: 924px; top: 221px; gap: 6px; }
  .cover-crewnest .social span { width: 17px; height: 17px; }
  .avatar-crewnest { left: 174px; top: 690px; width: 148px; height: 148px; }
  .avatar-crewnest .brand { font-size: 25px; }

  /* Pagewall */
  .cover-pagewall .brand { left: 12px; top: 10px; font-size: 14px; }
  .cover-pagewall .headline { font-size: 27px; }
  .cover-pagewall .line-one { left: 21px; top: 53px; }
  .cover-pagewall .line-two { left: 67px; top: 84px; }
  .cover-pagewall .pitch { left: 129px; top: 119px; font-size: 7.2px; line-height: 8.8px; }
  .cover-pagewall .call-box { left: 183px; top: 153px; width: 129px; height: 14px; font-size: 7.4px; }
  .cover-pagewall .call-box b { font-size: 9.2px; }
  .cover-pagewall .partner { top: 9px; font-size: 11px; }
  .cover-pagewall .partner-tag { font-size: 5.2px; }
  .cover-pagewall .partner-one { left: 389px; width: 64px; }
  .cover-pagewall .partner-two { left: 461px; width: 64px; }
  .cover-pagewall .inset-photo { left: 361px; top: 77px; width: 99px; height: 99px; border-width: 3px; }
  .cover-pagewall .inset-bracket { left: 354px; top: 145px; width: 32px; height: 37px; }
  .cover-pagewall .social { left: 476px; top: 177px; gap: 5px; }
  .cover-pagewall .social span { width: 13px; height: 13px; }
  .avatar-pagewall { left: 132px; top: 1041px; width: 102px; height: 102px; }
  .avatar-pagewall .brand { font-size: 16px; }
</style>
</head>
<body>

  <p class="cover-label" style="top:36px">Blipster Cover</p>
  <section class="cover cover-blipster">
    <div class="backdrop">
      <div class="office-photo" role="img" aria-label="Faded office desk photo with invoice on a monitor and pen holder"></div>
      <svg class="shapes" viewBox="0 0 950 316" preserveAspectRatio="none" role="img" aria-label="Green-tinted photo of hands working with documents">
        <defs><linearGradient id="greenBlip" x1="0" y1="0" x2="1" y2="1"><stop offset="0" stop-color="#54a748"/><stop offset="1" stop-color="#3f8d35"/></linearGradient></defs>
        <polygon points="614,0 950,0 950,316 831,316" fill="url(#greenBlip)"/>
        <polygon points="598,0 606,0 816,316 806,316" fill="var(--green)"/>
      </svg>
    </div>
    <div class="brand"><span class="brand-square"></span><span class="brand-name">Halvard<br>Ledger</span></div>
    <h1 class="headline line-one">Increase Cash Flow,</h1>
    <h2 class="headline line-two"><span class="accent">GROW</span> Your <span class="accent">Business!</span></h2>
    <p class="pitch">We help companies eliminate credit risk, improve cash flow,<br>and grow their business by providing flexible factoring<br>solutions. <strong>Get Funded, Keep Going!</strong></p>
    <div class="call-box">Call Us Today : <b>555.013.2468</b></div>
    <div class="partner partner-one partner-bold"><span class="partner-name">Fleetrun</span><span class="partner-tag">Made for Road Crews</span></div>
    <div class="partner partner-two"><span class="partner-name">Fleetrun</span><span class="partner-tag">Made for Road Crews</span></div>
    <div class="inset-bracket"></div>
    <div class="inset-photo" role="img" aria-label="Close-up of a finger pressing calculator keys"></div>
    <div class="social" aria-label="Social profiles"><span></span><span></span><span></span></div>
  </section>
  <div class="avatar avatar-blipster"><div class="brand"><span class="brand-square"></span><span class="brand-name">Halvard<br>Ledger</span></div></div>

  <p class="cover-label" style="top:486px">Crewnest Cover</p>
  <section class="cover cover-crewnest">
    <div class="backdrop">
      <div class="office-photo" role="img" aria-label="Faded office desk photo with invoice on a monitor and pen holder"></div>
      <svg class="shapes" viewBox="0 0 1003 250" preserveAspectRatio="none" role="img" aria-label="Green-tinted photo of hands working with documents">
        <defs><linearGradient id="greenCrew" x1="0" y1="0" x2="1" y2="1"><stop offset="0" stop-color="#54a748"/><stop offset="1" stop-color="#3f8d35"/></linearGradient></defs>
        <polygon points="738,0 1003,0 1003,250 909,250" fill="url(#greenCrew)"/>
        <polygon points="722,0 729,0 895,250 887,250" fill="var(--green)"/>
      </svg>
    </div>
    <div class="brand"><span class="brand-square"></span><span class="brand-name">Halvard<br>Ledger</span></div>
    <h1 class="headline line-one">Increase Cash Flow,</h1>
    <h2 class="headline line-two"><span class="accent">GROW</span> Your <span class="accent">Business!</span></h2>
    <p class="pitch">We help companies eliminate credit risk, improve cash flow,<br>and grow their business by providing flexible factoring<br>solutions. <strong>Get Funded, Keep Going!</strong></p>
    <div class="call-box">Call Us Today : <b>555.013.2468</b></div>
    <div class="partner partner-one partner-bold"><span class="partner-name">Fleetrun</span><span class="partner-tag">Made for Road Crews</span></div>
    <div class="partner partner-two"><span class="partner-name">Fleetrun</span><span class="partner-tag">Made for Road Crews</span></div>
    <div class="inset-bracket"></div>
    <div class="inset-photo" role="img" aria-label="Close-up of a finger pressing calculator keys"></div>
    <div class="social" aria-label="Social profiles"><span></span><span></span><span></span></div>
  </section>
  <div class="avatar avatar-crewnest"><div class="brand"><span class="brand-square"></span><span class="brand-name">Halvard<br>Ledger</span></div></div>

  <p class="cover-label" style="top:875px">Pagewall Cover</p>
  <section class="cover cover-pagewall">
    <div class="backdrop">
      <div class="office-photo" role="img" aria-label="Faded office desk photo with invoice on a monitor and pen holder"></div>
      <svg class="shapes" viewBox="0 0 539 200" preserveAspectRatio="none" role="img" aria-label="Green-tinted photo of hands working with documents">
        <defs><linearGradient id="greenPage" x1="0" y1="0" x2="1" y2="1"><stop offset="0" stop-color="#54a748"/><stop offset="1" stop-color="#3f8d35"/></linearGradient></defs>
        <polygon points="323,0 539,0 539,200 463,200" fill="url(#greenPage)"/>
        <polygon points="311,0 316,0 453,200 447,200" fill="var(--green)"/>
      </svg>
    </div>
    <div class="brand"><span class="brand-square"></span><span class="brand-name">Halvard<br>Ledger</span></div>
    <h1 class="headline line-one">Increase Cash Flow,</h1>
    <h2 class="headline line-two"><span class="accent">GROW</span> Your <span class="accent">Business!</span></h2>
    <p class="pitch">We help companies eliminate credit risk, improve cash flow,<br>and grow their business by providing flexible factoring<br>solutions. <strong>Get Funded, Keep Going!</strong></p>
    <div class="call-box">Call Us Today : <b>555.013.2468</b></div>
    <div class="partner partner-one partner-bold"><span class="partner-name">Fleetrun</span><span class="partner-tag">Made for Road Crews</span></div>
    <div class="partner partner-two"><span class="partner-name">Fleetrun</span><span class="partner-tag">Made for Road Crews</span></div>
    <div class="inset-bracket"></div>
    <div class="inset-photo" role="img" aria-label="Close-up of a finger pressing calculator keys"></div>
    <div class="social" aria-label="Social profiles"><span></span><span></span><span></span></div>
  </section>
  <div class="avatar avatar-pagewall"><div class="brand"><span class="brand-square"></span><span class="brand-name">Halvard<br>Ledger</span></div></div>

</body>
</html>
```